Packaging design for HOT NEW RETAIL BEARD OIL BRAND - Merrow Dalton Apothecary

Packaging design for beard oils. I've attached a brief, and I've also attached a few examples of bottles and boxes. Of course, we need an entirely unique look. I've attached the photo of Merrow Dalton as well - you can choose to use it or not (I'm open).

This product will be sold at national retailers and needs to look like a brand that is sold at boutique

What the consumer wants to see on the shelf:
-Box should larger than others and be soft touch (feels luxurious)
-More “hipster look/feel”
-Text should stand out like inspiration photos - jumping off the shelf to the consumer
-Use the existing logo of Merrow Dalton
-Deco will be wrap label as shown in current product image
-Sample text to pull copy for outer carton (taken from label on glass bottle):
-Strengthen and condition your beard with this blend of natural oils. Sunflower oil is rich in omega, fatty acids and vitamins E, C, B, and A, while avocado oil hydrates the beard fibers from root to tip, keep the beard looking and feeling extraordinary. Smooth into your beard for a healthy sheen and a woodsy scent evoking the great outdoors.
-Cool/Hipster product at discount pricing

Target Market(s)

Men from ages 20-40. Women also buy this product for their men, so it needs to look like a well known brand.

Industry/Entity Type

Hair And Beauty

Font styles to use
Sans Serif

Colors

Designer to choose colors to be used in the design.

Requirements
Must have
• A full label and box design with key call outs:
• Features and benefits - found in attached brief
• Description of what it is: Beard Oil
• Name of frangrance: Sandalwood
• Size: 2 oz / 60 ml
Nice to have
• Feel free to revamp the logo if needed. I am not married to the font for Merrow Dalton Apothecary.

```html
<!DOCTYPE html>
<html lang="en">
<head>
<meta charset="utf-8">
<title>Merrow Dalton Apothecary – Men's Beard Oil Packaging</title>
<link rel="stylesheet" href="https://fonts.googleapis.com/css2?family=Oswald:wght@500;600&family=Roboto+Condensed:wght@600&family=Libre+Baskerville:wght@400;700&display=swap">
<style>
  :root {
    --stage: #e6e2dc;
    --navy: #1d2b3a;
    --navy-deep: #15202c;
    --cream: #e9e4da;
    --copper-light: #e2b66f;
    --copper: #b7844a;
    --copper-dark: #7a5230;
    --portrait-light: #5a7aa0;
    --portrait-dark: #1c2c44;
  }
  * { box-sizing: border-box; margin: 0; padding: 0; }
  html, body { width: 1200px; height: 800px; overflow: hidden; }
  body {
    background: var(--stage);
    display: flex;
    align-items: center;
    justify-content: center;
    gap: 80px;
  }

  .carton, .bottle-label {
    background: radial-gradient(ellipse at 50% 35%, #24354a 0%, var(--navy) 55%, var(--navy-deep) 100%);
    color: var(--cream);
    display: flex;
    flex-direction: column;
    align-items: center;
    text-align: center;
  }

  .carton { width: 360px; height: 740px; padding: 22px 26px 0; }
  .bottle-label { width: 300px; height: 400px; padding: 14px 22px 0; }

  .accent-band {
    width: 100%;
    height: 8px;
    background: linear-gradient(90deg, var(--copper-dark), var(--copper-light), var(--copper), var(--copper-light), var(--copper-dark));
  }
  .bottle-label .accent-band { height: 6px; }

  .brand {
    font-family: "Libre Baskerville", serif;
    font-weight: 700;
    color: var(--cream);
    text-transform: uppercase;
    line-height: 1.05;
  }
  .carton .brand { font-size: 22px; letter-spacing: 2px; margin-top: 26px; }
  .bottle-label .brand { font-size: 17px; letter-spacing: 1.5px; margin-top: 16px; }
  .brand-sub { display: block; font-size: 0.42em; letter-spacing: 1.5px; margin-top: 6px; }

  .portrait {
    width: 132px; height: 132px;
    border-radius: 50%;
    border: 2px solid var(--cream);
    background: radial-gradient(circle at 50% 40%, var(--portrait-light), var(--portrait-dark) 75%);
    margin-top: 22px;
  }

  .product-name {
    font-family: "Oswald", sans-serif;
    font-weight: 600;
    text-transform: uppercase;
    line-height: 0.98;
    background: linear-gradient(180deg, var(--copper-light) 0%, var(--copper) 55%, var(--copper-dark) 100%);
    -webkit-background-clip: text;
    background-clip: text;
    color: transparent;
  }
  .product-name .line-1 { display: block; }
  .product-name .line-2 { display: block; }
  .carton .product-name { margin-top: 18px; }
  .carton .line-1 { font-size: 62px; }
  .carton .line-2 { font-size: 76px; }
  .bottle-label .product-name { margin-top: 16px; }
  .bottle-label .line-1 { font-size: 40px; }
  .bottle-label .line-2 { font-size: 50px; }

  .scent {
    display: flex;
    align-items: center;
    gap: 8px;
    width: 100%;
    border-top: 2px solid var(--cream);
    border-bottom: 2px solid var(--cream);
    font-family: "Libre Baskerville", serif;
    letter-spacing: 2px;
    text-transform: uppercase;
    color: var(--cream);
  }
  .scent::before, .scent::after {
    content: "";
    flex: 1;
    align-self: stretch;
    margin: 4px 0;
    background: repeating-linear-gradient(180deg, var(--cream) 0 1px, transparent 1px 4px);
  }
  .carton .scent { font-size: 20px; padding: 4px 0; margin-top: 16px; }
  .bottle-label .scent { font-size: 14px; padding: 3px 0; margin-top: 12px; width: 88%; }

  .callouts {
    font-family: "Libre Baskerville", serif;
    text-transform: uppercase;
    line-height: 1.65;
    color: var(--cream);
  }
  .carton .callouts {
    font-size: 16px;
    margin-top: 18px;
    padding-bottom: 10px;
    width: 100%;
    border-bottom: 2px solid var(--cream);
  }
  .bottle-label .callouts { font-size: 11px; margin-top: 10px; line-height: 2.3; }

  .benefit {
    font-family: "Roboto Condensed", sans-serif;
    font-weight: 600;
    font-size: 17px;
    letter-spacing: 1px;
    line-height: 1.6;
    text-transform: uppercase;
    margin-top: 20px;
  }

  .carton .accent-band.bottom { margin-top: 22px; }
  .bottle-label .accent-band.bottom { margin-top: 8px; }

  .size {
    font-family: "Oswald", sans-serif;
    font-weight: 500;
    color: var(--cream);
  }
  .carton .size { font-size: 22px; margin-top: 16px; }
  .bottle-label .size { font-size: 13px; margin-top: 8px; }
</style>
</head>
<body>

  <section class="carton" aria-label="Carton front">
    <div class="accent-band"></div>
    <h1 class="brand">Merrow<br>Dalton<span class="brand-sub">Apothecary</span></h1>
    <div class="portrait" role="img" aria-label="Circular portrait photo of a bearded man"></div>
    <h2 class="product-name"><span class="line-1">Men’s</span><span class="line-2">Beard Oil</span></h2>
    <p class="scent">Sandalwood</p>
    <p class="callouts">For all beard types<br>100% Naturals</p>
    <p class="benefit">Strengthen and condition<br>your beard with this blend<br>of natural oils</p>
    <div class="accent-band bottom"></div>
    <p class="size">2 oz / 60 ml</p>
  </section>

  <section class="bottle-label" aria-label="Bottle wrap label">
    <div class="accent-band"></div>
    <h1 class="brand">Merrow<br>Dalton<span class="brand-sub">Apothecary</span></h1>
    <h2 class="product-name"><span class="line-1">Men’s</span><span class="line-2">Beard Oil</span></h2>
    <p class="scent">Sandalwood</p>
    <p class="callouts">For all beard types<br>100% Naturals</p>
    <div class="accent-band bottom"></div>
    <p class="size">2 oz / 60 ml</p>
  </section>

</body>
</html>
```